Brightwell Homes needs a web design and brand identifier

Brightwell Homes is a pioneering approach by Victorian councils and four greenhouse alliances to support low income households to install solar systems with no upfront costs.

Brightwell Homes will commence in May 2017.

Brightwell Homes is looking for a designer to create a website banner incorporating a brand identifier for Brightwell Homes. The brand identifier will be used in Brightwell Homes promotional materials, such as flyers and mail outs.

The website banner and brand identifier should engender trust and confidence in the target group (retirees).
Updates

Project Deadline Extended
Reason: Hi, Thank you for your work so far. We've been given advice to get a separate logo designed (instead of trying to include this as part of the banner design). Sorry for not realising this until now - we're new to all this. So, I have a couple of preliminary logo designs that are being considered by our project control group. I will forward a copy of the logo once we have it. The project control group is looking for a web design that is unique to Brightwell Homes and a design that draws on the key elements of the program (i.e. it helps people save money and take control). The site should be friendly but not too informal as the target group is seniors. Here's a link to another community energy organisation: www.kestrelgrid.com.au/ Apologies again for the delays. Cheers, Doug

Target Market(s)

Home owning, low income, retirees

Industry/Entity Type

Non Profit

Number of Pages Required

1 page

Font styles to use
Sans Serif

Requirements
Must have
• Use of Brightwell Home name
• Must promote Brightwell Homes as safe, reliable and trustworthy
Nice to have
• Blue - to engender sense of safety and confidence (open to suggestions, though)
• Solar panels / the sun
Should not have
• Anything that is hard to read
• anything that promotes riskyness

```html
<!DOCTYPE html>
<html lang="en">
<head>
<meta charset="utf-8">
<title>Brightwell Homes</title>
<link rel="stylesheet" href="https://fonts.googleapis.com/css2?family=Titillium+Web:wght@400;600;700&family=Open+Sans:wght@400;600;700&display=swap">
<style>
:root{
  --blue:#1a8ee8;
  --blue-bright:#1e9bf0;
  --blue-deep:#0f6fc4;
  --navy:#0c1b2a;
  --ink:#222;
  --muted:#666;
  --line:#9cc9ef;
  --card-line:#cfd8e0;
  --grey-band:#eceeef;
  --footer:#2c8ad6;
  --white:#fff;
}
*{box-sizing:border-box;margin:0;padding:0}
html,body{width:1200px;height:3098px;overflow:hidden}
body{font-family:"Open Sans",Arial,sans-serif;color:var(--ink);background:var(--white);position:relative}
.heading{font-family:"Titillium Web",Arial,sans-serif}
section,header,footer{position:absolute;left:0;width:1200px}

/* header */
.site-header{top:0;height:95px;background:var(--navy);z-index:3}
.brand{position:absolute;left:0;top:0;width:444px;height:95px;background:var(--blue-bright);clip-path:polygon(0 0,100% 0,88% 100%,0 100%);display:flex;align-items:center;padding-left:171px}
.brand span{font-family:"Titillium Web",Arial,sans-serif;font-weight:700;font-size:31px;color:var(--white);letter-spacing:.5px}
.call{position:absolute;left:680px;top:10px;display:flex;align-items:center;gap:12px;color:var(--white)}
.call small{display:block;font-size:10px;font-weight:600;letter-spacing:.5px}
.call strong{display:block;font-family:"Titillium Web",Arial,sans-serif;font-size:22px;line-height:22px}
.quote-btn{position:absolute;left:888px;top:17px;width:138px;height:30px;border-radius:15px;background:var(--blue-bright);color:var(--white);font-size:11px;font-weight:700;display:flex;align-items:center;justify-content:center}
.main-nav{position:absolute;right:174px;top:68px;display:flex;gap:30px}
.main-nav a{color:var(--white);font-size:11px;font-weight:700;text-decoration:none;letter-spacing:.3px}

/* hero */
.hero{top:95px;height:506px;background:linear-gradient(100deg,#1c3d6b 0%,#2f5f93 30%,#6c7d6a 55%,#7d9a5a 80%,#476b3a 100%)}
.hero-photo{position:absolute;inset:0}
.hero-copy{position:absolute;left:171px;top:142px;color:var(--white)}
.hero-copy .kicker{font-family:"Titillium Web",Arial,sans-serif;font-size:24px;letter-spacing:.5px;text-transform:uppercase}
.hero-copy h1{font-family:"Titillium Web",Arial,sans-serif;font-weight:700;font-size:64px;line-height:60px;margin-top:2px}
.hero-copy p{font-size:16px;line-height:26px;width:470px;margin-top:28px}
.hero-phone{display:flex;align-items:center;gap:12px;margin-top:20px;font-family:"Titillium Web",Arial,sans-serif;font-weight:700;font-size:26px}

/* section titles */
.section-title{font-family:"Titillium Web",Arial,sans-serif;font-weight:700;text-align:center;font-size:30px;text-transform:uppercase}
.section-title::after{content:"";display:block;width:52px;height:3px;background:var(--blue);margin:12px auto 0}

/* welcome */
.welcome{top:601px;height:446px}
.welcome .section-title{margin-top:60px;color:#111}
.video{position:absolute;left:171px;top:147px;width:428px;height:237px;background:linear-gradient(180deg,#7d9a94,#6e8b86 60%,#7f9c7a)}
.play{position:absolute;left:50%;top:50%;transform:translate(-50%,-60%)}
.video-label{position:absolute;left:0;right:0;top:158px;text-align:center;color:var(--white);font-size:12px;font-weight:700}
.welcome-text{position:absolute;left:632px;top:147px;width:355px;font-size:13px;line-height:22px;color:var(--muted)}
.welcome-text p+p{margin-top:18px}

/* how it works */
.how{top:1047px;height:440px;background:linear-gradient(180deg,var(--blue-bright),#1787e0)}
.how .section-title{margin-top:52px;color:var(--white);font-size:26px}
.how .section-title::after{background:var(--white)}
.steps-line{position:absolute;left:171px;top:203px}
.step{position:absolute;top:203px;width:180px;text-align:center;color:var(--white)}
.step .icon{width:112px;height:112px;border-radius:50%;background:var(--white);border:6px solid #8cc6f3;margin:0 auto;display:flex;align-items:center;justify-content:center}
.step p{font-size:12px;line-height:21px;margin-top:30px}

/* eligibility */
.eligible{top:1487px;height:330px}
.eligible .section-title{margin-top:56px;font-size:26px;color:#111}
.eligible .section-title::after{display:none}
.eligible .sub{text-align:center;font-size:12px;color:var(--muted);margin-top:2px}
.cards{position:absolute;left:173px;top:142px;display:flex;gap:24px}
.card{width:195px;height:126px;border:2px solid var(--card-line);border-radius:40px 0 40px 0;display:flex;align-items:center;justify-content:center;text-align:center;font-size:12px;font-weight:700;color:#444;line-height:18px}

/* who */
.who{top:1817px;height:471px;background:linear-gradient(180deg,#2f8fe6 0%,#5fb0f0 35%,#2c4f85 70%,#c55a2a 100%)}
.who-copy{position:absolute;left:171px;top:58px;color:var(--white)}
.who-copy h2{font-family:"Titillium Web",Arial,sans-serif;font-weight:700;font-size:30px}
.who-copy p{font-size:13px;line-height:21px;width:500px;margin-top:4px}

/* what next */
.next{top:2288px;height:318px}
.next-frame{position:absolute;left:171px;top:93px;width:856px;height:160px;border-top:2px solid var(--line);border-bottom:2px solid var(--line)}
.next-tab{position:absolute;left:50%;top:-34px;transform:translateX(-50%);background:var(--white);border:2px solid var(--line);border-bottom:none;padding:4px 26px;font-family:"Titillium Web",Arial,sans-serif;font-weight:700;font-size:24px;color:#111}
.next-body{position:absolute;left:0;right:0;top:26px;text-align:center}
.next-body .lead{font-size:13px;color:var(--muted)}
.next-body .contact{font-family:"Titillium Web",Arial,sans-serif;font-size:25px;font-weight:600;margin-top:6px;line-height:34px}
.next-body .contact b{color:var(--blue);font-weight:700}

/* partners */
.partners{top:2606px;height:227px;background:var(--grey-band)}
.partners .section-title{margin-top:42px;font-size:18px;color:#111}
.partner-badges{position:absolute;left:0;right:0;top:118px;display:flex;justify-content:center;gap:40px;align-items:center}
.badge{background:#c9cdd1;border-radius:4px}

/* footer */
.site-footer{top:2833px;height:265px;background:var(--footer);color:var(--white);font-size:11px}
.col{position:absolute;top:32px}
.col h4{font-size:11px;font-weight:700;margin-bottom:16px;text-transform:uppercase}
.col li{list-style:none;line-height:23px}
.contact-row{display:flex;gap:10px;margin-bottom:10px;line-height:16px}
.social{display:flex;gap:14px}
.social span{width:20px;height:20px;border:2px solid var(--white);border-radius:50%}
.signup input{display:block;width:196px;height:32px;border:none;margin-bottom:8px;padding-left:10px;font-size:11px;font-family:inherit}
.signup button{width:196px;height:32px;background:#0d4f8a;color:var(--white);border:none;font-weight:700;font-size:12px;font-family:inherit}
.copyright{position:absolute;left:171px;top:244px;font-size:10px}
</style>
</head>
<body>

<header class="site-header">
  <div class="brand"><span>BRIGHTWELL HOMES</span></div>
  <div class="call">
    <svg width="22" height="22" viewBox="0 0 24 24" fill="none" stroke="#fff" stroke-width="2"><path d="M5 3h4l2 5-3 2a12 12 0 0 0 6 6l2-3 5 2v4a2 2 0 0 1-2 2A17 17 0 0 1 3 5a2 2 0 0 1 2-2z"/></svg>
    <div><small>CALL NOW</small><strong>0400 555 270</strong></div>
  </div>
  <a class="quote-btn">REQUEST A QUOTE</a>
  <nav class="main-nav"><a>HOME</a><a>ABOUT US</a><a>SERVICES</a><a>HOW IT WORKS</a><a>CONTACT US</a></nav>
</header>

<section class="hero">
  <div class="hero-photo" role="img" aria-label="Photo of a smiling senior man leaning on a fence in front of a tiled-roof house with solar panels"></div>
  <div class="hero-copy">
    <div class="kicker">Help pensioner households to</div>
    <h1>SAVE MONEY</h1>
    <p>And take control of their energy bills by installing an affordable, quality solar system and be part of an Australian first</p>
    <div class="hero-phone">
      <svg width="22" height="22" viewBox="0 0 24 24" fill="none" stroke="#fff" stroke-width="2"><path d="M5 3h4l2 5-3 2a12 12 0 0 0 6 6l2-3 5 2v4a2 2 0 0 1-2 2A17 17 0 0 1 3 5a2 2 0 0 1 2-2z"/></svg>
      0400 555 270
    </div>
  </div>
</section>

<section class="welcome">
  <h2 class="section-title">Welcome to Brightwell Homes</h2>
  <div class="video" role="img" aria-label="Video thumbnail illustration of a house with solar panels and wind turbines">
    <svg class="play" width="66" height="66" viewBox="0 0 66 66"><circle cx="33" cy="33" r="30" fill="none" stroke="#fff" stroke-width="3"/><path d="M26 20 L47 33 L26 46Z" fill="#fff"/></svg>
    <div class="video-label">WATCH VIDEO</div>
  </div>
  <div class="welcome-text">
    <p>We need you Help pensioner households to save money and take control of their energy bills by installing anaffordable, quality solar system and be part of an Australian first.</p>
    <p>Brightwell Homes is a pioneering approach by Victorian councils to support pensioner households to install solar with no upfront costs. We've done the hard work of finding a safe, reliable and quality installer so pensioners don't have to.</p>
  </div>
</section>

<section class="how">
  <h2 class="section-title">How it works</h2>
  <svg class="steps-line" width="856" height="112" viewBox="0 0 856 112">
    <g stroke="#7cc0f4" stroke-width="1.5" fill="none">
      <line x1="0" y1="56" x2="40" y2="56"/>
      <line x1="160" y1="56" x2="260" y2="56"/><path d="M200 50l6 6-6 6"/>
      <line x1="380" y1="56" x2="480" y2="56"/><path d="M420 50l6 6-6 6"/>
      <line x1="598" y1="56" x2="698" y2="56"/><path d="M638 50l6 6-6 6"/>
      <line x1="816" y1="56" x2="856" y2="56"/>
    </g>
  </svg>
  <div class="step" style="left:180px">
    <div class="icon"><svg width="50" height="50" viewBox="0 0 50 50" fill="none" stroke="#1a8ee8" stroke-width="2"><circle cx="20" cy="22" r="9"/><path d="M20 6v5M20 33v5M4 22h5M31 22h5M9 11l3 3M28 30l3 3M9 33l3-3M28 14l3-3"/><path d="M36 36h8M40 32v8"/></svg></div>
    <p>Brightwell Homes checks that every person gets a solar system that pays for itself in energy savings from day one</p>
  </div>
  <div class="step" style="left:399px">
    <div class="icon"><svg width="50" height="50" viewBox="0 0 50 50" fill="none" stroke="#1a8ee8" stroke-width="2"><rect x="10" y="6" width="24" height="20"/><path d="M18 6v20M26 6v20M10 13h24M10 20h24M22 26v8"/><rect x="24" y="32" width="18" height="12"/><path d="M24 37h18"/></svg></div>
    <p>Brightwell Homes organises for the solar system to be installed</p>
  </div>
  <div class="step" style="left:618px">
    <div class="icon"><svg width="50" height="50" viewBox="0 0 50 50" fill="none" stroke="#1a8ee8" stroke-width="2"><circle cx="25" cy="16" r="8"/><path d="M11 44c0-9 6-15 14-15s14 6 14 15"/><path d="M38 20l6-6"/></svg></div>
    <p>Brightwell Homes supports pensioners to understand and get the most out of solar</p>
  </div>
  <div class="step" style="left:837px">
    <div class="icon"><svg width="50" height="50" viewBox="0 0 50 50" fill="none" stroke="#1a8ee8" stroke-width="2"><path d="M8 36l8-14h18l8 14z"/><path d="M19 22l-3 14M31 22l3 14M12 29h26M25 36v8M17 44h16"/><text x="17" y="16" font-size="11" font-family="Open Sans,sans-serif" fill="#1a8ee8" stroke="none" font-weight="700">0%</text></svg></div>
    <p>Pensioners gradually pay for cost through their usual rates payments at 0% interest</p>
  </div>
</section>

<section class="eligible">
  <h2 class="section-title">Is my client eligible?</h2>
  <p class="sub">Refer clients who are:</p>
  <div class="cards">
    <div class="card">HOMEOWNERS</div>
    <div class="card">PENSION CARD<br>HOLDERS</div>
    <div class="card">USUALLY AT HOME<br>FROM 9AM TO 5PM</div>
    <div class="card">AVERAGE TO HIGH<br>ELECTRICITY USERS</div>
  </div>
</section>

<section class="who" role="img" aria-label="Photo of solar panels on an orange tiled roof under a bright blue sky with the sun">
  <div class="who-copy">
    <h2>WHO IS BRIGHTWELL HOMES?</h2>
    <p>Over 20 Victorian councils have come together with support from the Victorian Government's Clean Power Jobs Fund to run the Brightwell Home program.</p>
  </div>
</section>

<section class="next">
  <div class="next-frame">
    <div class="next-tab">WHAT NEXT?</div>
    <div class="next-body">
      <p class="lead">To refer clients or for further information, contact Doug Mercer at Brightwell Homes:</p>
      <p class="contact"><b>CALL US :</b> 0400 555 270<br><b>EMAIL US :</b> doug.mercer@eastvale.vic.gov.au</p>
    </div>
  </div>
</section>

<section class="partners">
  <h2 class="section-title">Brightwell Homes is a partnership between</h2>
  <div class="partner-badges">
    <div class="badge" style="width:150px;height:70px"></div>
    <div class="badge" style="width:190px;height:50px"></div>
    <div class="badge" style="width:170px;height:56px"></div>
    <div class="badge" style="width:110px;height:60px"></div>
  </div>
</section>

<footer class="site-footer">
  <div class="col" style="left:171px"><h4>Quick Links</h4><ul><li>Home</li><li>About Us</li><li>Services</li><li>How It Works</li><li>Contact Us</li></ul></div>
  <div class="col" style="left:295px"><h4>Support</h4><ul><li>Contact us</li><li>FAQs</li><li>Legal</li><li>Privacy Policy</li><li>Legal</li></ul></div>
  <div class="col" style="left:415px"><h4>Contact Us</h4>
    <div class="contact-row"><svg width="20" height="20" viewBox="0 0 20 20" fill="none" stroke="#fff" stroke-width="1.5"><circle cx="10" cy="10" r="9"/><path d="M10 15s-4-4-4-7a4 4 0 0 1 8 0c0 3-4 7-4 7z"/></svg><div>Your Company LTD.<br>Street Name, 000000<br>City Name</div></div>
    <div class="contact-row"><svg width="20" height="20" viewBox="0 0 20 20" fill="none" stroke="#fff" stroke-width="1.5"><circle cx="10" cy="10" r="9"/><path d="M7 5h2l1 3-1.5 1a6 6 0 0 0 3 3L13 11l3 1v2"/></svg><div>Phone<br>0400 555 270</div></div>
    <div class="contact-row"><svg width="20" height="20" viewBox="0 0 20 20" fill="none" stroke="#fff" stroke-width="1.5"><circle cx="10" cy="10" r="9"/><rect x="5" y="7" width="10" height="7"/><path d="M5 7l5 4 5-4"/></svg><div>Email<br>doug.mercer@eastvale.vic.gov.au</div></div>
  </div>
  <div class="col" style="left:646px"><h4>Get Connected</h4><div class="social"><span></span><span></span><span></span><span></span></div></div>
  <div class="col signup" style="left:830px"><h4>E-Newsletter Signup</h4><input placeholder="Name"><input placeholder="Email"><button>JOIN</button></div>
  <p class="copyright">© 2017 Brightwell Homes. All Rights Reserved</p>
</footer>

</body>
</html>
```